Health Tech Company needs a better formated document for a customer project

Please use this excel spreadsheet and format a better looking word document to share with the customer.

```html
<!DOCTYPE html>
<html lang="en">
<head>
<meta charset="utf-8">
<title>AZ Escalation Guide</title>
<link href="https://fonts.googleapis.com/css2?family=Open+Sans:wght@300;400;600&family=Roboto+Condensed:ital,wght@0,400;0,700;1,400;1,700&display=swap" rel="stylesheet">
<style>
  :root{
    --backdrop:#b3b3b3;
    --paper:#ffffff;
    --ink:#1a1a1a;
    --brand-ink:#3a3a3a;
    --brand-dot:#29a8e0;
    --header-blue:#5a7fe3;
    --row-green:#22ff2e;
    --row-yellow:#f7ff33;
    --row-teal:#56c1c9;
    --rule:#3c3c3c;
    --band-sky:#29a8e0;
    --band-navy:#3a4f9a;
    --band-lime:#8bc53f;
  }
  *{box-sizing:border-box;margin:0;padding:0}
  html,body{width:1200px;height:939px;overflow:hidden}
  body{background:var(--backdrop);position:relative;font-family:"Roboto Condensed",sans-serif;color:var(--ink)}
  .page{position:absolute;width:486px;height:375px;background:var(--paper)}
  .page--one{left:90px;top:119px}
  .page--two{left:625px;top:445px}
  .brand{position:absolute;left:15px;top:13px;display:flex;align-items:center;gap:7px}
  .brand__dot{width:22px;height:22px;border-radius:50%;background:var(--brand-dot)}
  .brand__name{font-family:"Open Sans",sans-serif;font-weight:300;font-size:26px;color:var(--brand-ink);letter-spacing:.5px;line-height:1}
  .page__title{position:absolute;top:69px;left:0;width:100%;text-align:center;font-family:"Open Sans",sans-serif;font-weight:600;font-size:11.5px}
  .guide{position:absolute;left:26px;width:433px;border-collapse:collapse;table-layout:fixed;font-size:4.3px;line-height:1.55}
  .page--one .guide{top:90px}
  .page--two .guide{top:69px}
  .guide col.code{width:57px}
  .guide td,.guide th{border:0.6px solid var(--rule);vertical-align:top;padding:3px 3px;text-align:left}
  .guide th{background:var(--header-blue);color:#fff;font-weight:700;height:21px}
  .guide td:first-child{font-weight:700}
  .guide em{font-style:italic}
  .row--green td{background:var(--row-green)}
  .row--yellow td{background:var(--row-yellow)}
  .row--teal td{background:var(--row-teal)}
  .legend{position:absolute;left:26px;top:294px;font-size:4.4px;line-height:1.5}
  .legend__title{font-weight:700;text-decoration:underline}
  .legend u{text-decoration:underline}
  .page__url{position:absolute;right:27px;top:350px;font-family:"Open Sans",sans-serif;font-size:7px;color:var(--ink)}
  .bands{position:absolute;left:0;bottom:0;width:100%;height:10px;display:flex}
  .bands span{flex:1}
  .bands .sky{background:var(--band-sky)}
  .bands .navy{background:var(--band-navy)}
  .bands .lime{background:var(--band-lime)}
</style>
</head>
<body>

<section class="page page--one">
  <div class="brand"><span class="brand__dot"></span><span class="brand__name">veridane</span></div>
  <h1 class="page__title">AZ Escalation- Guide</h1>
  <table class="guide">
    <colgroup><col class="code"><col><col><col></colgroup>
    <tr>
      <th>Saguaro Health AZ Escalation Code</th>
      <th>Reason This Code Is Used</th>
      <th>Is rendering provider soft removed? (deactivated in the CRM) Y / N?</th>
      <th>CRM- Veridane action required</th>
    </tr>
    <tr class="row--green" style="height:34px">
      <td>Network Participation Question</td>
      <td><em>A. Escalation is done when clinic is unsure of network participation or has not heard of a specific plan (ie, Canyon Select, HMO)</em></td>
      <td><em>The providers information is still confirmed and marked as clean. Confirmed data will display on the weekly data extract and Network Participation question will be displayed on the weekly escalation report.</em></td>
      <td>Mark as clean</td>
    </tr>
    <tr class="row--yellow" style="height:54px">
      <td>Confirmation Needed- Provider No Longer Practicing at TIN</td>
      <td><em>A. Contact at provider office has notified us that the provider is not practicing under TIN that AZ has provided to Veridane<br>B. Contact at provider office or voicemail greeting has notified us that the provider has retired<br>C. Contact at provider office has notified us that the provider deceased</em></td>
      <td>Provider is soft removed from Veridane's CRM and removal is displayed on the weekly extract. Corresponding provider removal and available additional information are also displayed on the escalation report.</td>
      <td>Utilize the trash can icon to successfully remove the provider. Select Confirmation Needed- Provider No longer Practicing at TIN as your reason code. Please include phone number, office contact's first name and job title in the activity stream comment section of the removal page.</td>
    </tr>
    <tr class="row--green" style="height:40px">
      <td>Office Closed- Confirmation Needed</td>
      <td><em>A.Office appears to be closed; obtained info via voicemail, online search, etc</em></td>
      <td><em>Provider is <b>not</b> soft removed. Weekly extract report will show this provider group as cleaned, but not accepting new patients on the weekly extract. Office closed- Confirmation Needed will be listed on the weekly escalation report.</em></td>
      <td>Switch toggle to <b>NOT</b> accepting new patients; Mark as clean</td>
    </tr>
    <tr class="row--green" style="height:47px">
      <td>Non-Participation</td>
      <td><em>Contact at TIN states they are no longer participating with Saguaro Health AZ Advantage or commercial plans</em></td>
      <td><em>Provider is <b>not</b> soft removed. Weekly extract report will show this provider group as cleaned, but accepting new patients and Network participation will be showing as No on the weekly extract. "Medicaid or Medicare Non Participation" will be listed on the weekly escalation report.</em></td>
      <td>Switch toggle to <b>NOT</b> accepting new patients; Mark as clean</td>
    </tr>
    <tr class="row--green" style="height:40px">
      <td>Practice Name Issue</td>
      <td><em>Clinic is practicing under a new name</em></td>
      <td><em>Unless, provider group declines to clean, the providers information is still confirmed and marked as clean. Confirmed data will display on the weekly data extract and Practice Name Issue will be displayed on the weekly escalation report.</em></td>
      <td>Mark as clean, if the data was cleaned. Ask about the TIN, only clean if the TIN matches. If the TIN no longer matches, then use Not practicing under TIN and remove the providers.</td>
    </tr>
  </table>
  <p class="page__url">www.veridane.com</p>
  <div class="bands"><span class="sky"></span><span class="navy"></span><span class="lime"></span></div>
</section>

<section class="page page--two">
  <div class="brand"><span class="brand__dot"></span><span class="brand__name">veridane</span></div>
  <table class="guide">
    <colgroup><col class="code"><col><col><col></colgroup>
    <tr class="row--yellow" style="height:42px">
      <td>Other</td>
      <td><em>Misc items where we do not have an existing Escalation bucket code: For example: Clinic is self pay only, office contact has unsubscribed from our webforms.</em></td>
      <td>Details are only captured in the weekly escalation report</td>
      <td>Dependent on what is being escalated</td>
    </tr>
    <tr class="row--green" style="height:74px">
      <td>Phone number incorrect</td>
      <td><em>Clinic phone number is incorrect (disconnected and/ or for another provider group); unable to obtain phone number for actual TIN</em></td>
      <td><em>Provider is shown with no changes on the extract and escalation note of Phone number is incorrect is displayed on the escalation report. <b>Veridane will suppress the provider group from the call queue and wait for the correct phone number to be sent via a delta file. Escalation will be reflected on the escalation report</b></em></td>
      <td>Perform a Searchly search for phone number alternative. Do not mark as clean. If an alternate phone number is not found Escalate that a new phone number is needed. Format: <em>Called (paste in phone number that you called) state what happened. In addition, please specify whether we have an email address and if we have not received a response from the email that we sent or if their is no email address on file and then say "please provide alternate scheduling phone number"</em></td>
    </tr>
    <tr class="row--yellow" style="height:41px">
      <td>Do Not List in Directory</td>
      <td><em>A. Rendering provider or TIN is not to be listed in the Provider Directory<br>B.Reached an answering service for a hospitalist without an office for the provider</em></td>
      <td>Provider is soft removed from Veridane's CRM and removal is displayed on the weekly extract. Corresponding provider removal and available additional information are also displayed on the escalation report.</td>
      <td>Utilize the trash can icon to successfully remove the provider. Select Do Not Display in the Directory as your reason code. Please include phone number, office contact's first name and job title in the comment section of the removal page.</td>
    </tr>
    <tr class="row--teal" style="height:53px">
      <td>Reactivation</td>
      <td>A. CSR accidently removed a provider from a TIN<br>B. Contact reached back out to Veridane to let us know that they accidently removed a provider, via the webform<br>C. Healthplan reached out to Veridane to let us know that a contact accidently removed a provider, via the webform</td>
      <td>Provider is shown as cleaned (if they have been cleaned) and the accompanying escalation note will be displayed on both the Inbound/extract file and the weekly escalation report.</td>
      <td>Use three dots to reactivate user and include relevant details in activity stream</td>
    </tr>
  </table>
  <div class="legend">
    <p class="legend__title">Color Legend</p>
    <p>Rows highlighted in <u>yellow</u> are provider removal reasons that can be used when a Research Analyst using the trashcan feature in the CRM</p>
    <p>Rows highlighted in <u>gold</u> are used as both a provider removal reason and as a general escalation code in the CRM</p>
    <p>Rows highlighted in <u>green</u> are escalation codes that are not for removal and are instead used to share information with the health plan on their escalation report</p>
    <p>Rows highlighted in <u>teal</u> are system escalations that happen as a result of an action taken by a Research Analyst in the CRM</p>
  </div>
  <p class="page__url">www.veridane.com</p>
  <div class="bands"><span class="sky"></span><span class="navy"></span><span class="lime"></span></div>
</section>

</body>
</html>
```